Re-design existing website and add products for sale.

Our current website is very basic and cluttered. (brightwillowcare.com.au)We want a modern looking website that is easy to navigate. We also want to start selling essential oils and crystal products, so there needs to be a separate page for this. Also needs to be easily edited as we need to change the monthly oracle card with the description. Would like calming colours as we are all about natural healing. Alongside the services listed there should be a button to book now which asks for their name, email, phone number ect. and adds it to the cart.

• Logo is still being designed, please leave a space for the logo which will basically be a lotus flower within a mandala.

```html
<!DOCTYPE html>
<html lang="en">
<head>
<meta charset="utf-8">
<title>Bright Willow Care</title>
<link rel="stylesheet" href="https://fonts.googleapis.com/css2?family=Poppins:wght@500;600;700&family=Hind:wght@400;500&display=swap">
<style>
:root{
  --navy:#0c70b8;
  --sky:#00bdf2;
  --deep:#0a8fd1;
  --ink:#1a1a1a;
  --white:#ffffff;
}
*{margin:0;padding:0;box-sizing:border-box}
html,body{width:1200px;height:3571px;overflow:hidden}
body{position:relative;background:var(--white);font-family:"Hind",sans-serif;color:var(--ink);font-size:20px;line-height:1.2}
.abs{position:absolute}
.brand{font-family:"Poppins",sans-serif;font-weight:600;color:var(--navy);font-size:34px}
.nav{left:558px;top:48px;display:flex;gap:30px;font-family:"Poppins",sans-serif;font-weight:500;font-size:15px;color:var(--navy)}
.search{left:674px;top:10px;width:155px;height:22px;border:1.5px solid var(--navy);border-radius:11px;font-size:11px;color:#7aa6c9;padding:3px 0 0 26px}
.search svg{position:absolute;left:9px;top:5px}
.social{left:862px;top:8px;display:flex;gap:10px}
.social span{width:20px;height:20px;background:var(--navy);border-radius:3px}
.hero{left:0;top:95px;width:1200px;height:529px;background:linear-gradient(170deg,var(--sky) 0%,var(--sky) 45%,var(--deep) 100%);overflow:hidden}
.hero-text{left:233px;top:178px;width:450px;color:var(--white);font-size:19px;line-height:1.22}
.btn{position:absolute;display:flex;align-items:center;justify-content:center;font-family:"Poppins",sans-serif;font-weight:600;font-size:17px;letter-spacing:.5px}
.btn-outline{border:2.5px solid var(--white);color:var(--white);border-radius:6px}
.btn-solid{background:var(--sky);color:var(--white);border-radius:6px}
.photo{position:absolute}
.title{position:absolute;left:0;width:1200px;text-align:center;font-family:"Poppins",sans-serif;font-weight:700;color:var(--navy);font-size:44px}
.copy{font-size:19.5px;line-height:1.2}
.service{width:165px;font-size:15px;line-height:1.25}
.service svg{display:block;margin:0 0 14px 64px}
.checks{left:233px;top:2052px;width:380px;list-style:none}
.checks li{position:relative;padding-left:36px;margin-bottom:6px;font-size:19.5px;line-height:1.2}
.checks svg{position:absolute;left:2px;top:2px}
.thumb{width:92px;height:94px;background:linear-gradient(160deg,#6b5a48,#2a2e45 55%,#1d7a6a)}
.cta{left:0;top:2381px;width:1200px;height:436px;background:linear-gradient(170deg,var(--sky) 0%,var(--sky) 50%,var(--deep) 100%);overflow:hidden}
.cta-title{left:475px;top:123px;width:536px;text-align:center;font-family:"Poppins",sans-serif;font-weight:700;font-size:45px;line-height:1.22;color:var(--white)}
.field{position:absolute;left:631px;width:333px;border:2.5px solid var(--sky);border-radius:5px;background:var(--white);font-size:19px}
.field .tag{position:absolute;left:0;top:0;bottom:0;width:56px;background:var(--navy);display:flex;align-items:center;justify-content:center}
.field .label{position:absolute;left:68px;top:5px}
.footer{left:0;top:3438px;width:1200px;height:133px;background:var(--sky);color:var(--white)}
.footer h4{font-family:"Poppins",sans-serif;font-weight:600;font-size:14px}
.footer p{font-size:11.5px;line-height:1.25}
.footer-brand{left:233px;top:46px;font-family:"Poppins",sans-serif;font-weight:600;font-size:20px}
.sq{display:inline-block;width:20px;height:20px;background:var(--white);border-radius:3px;margin-right:8px}
</style>
</head>
<body>

<header>
  <div class="abs brand" style="left:233px;top:18px">Bright Willow</div>
  <div class="abs search"><svg width="11" height="11" viewBox="0 0 11 11"><circle cx="4.5" cy="4.5" r="3.5" fill="none" stroke="#0c70b8" stroke-width="1.5"/><line x1="7" y1="7" x2="10" y2="10" stroke="#0c70b8" stroke-width="1.5"/></svg>Search</div>
  <div class="abs social"><span></span><span></span><span></span><span></span></div>
  <nav class="abs nav"><span>Home</span><span>About Us</span><span>Products</span><span>Services</span><span>Contact Us</span></nav>
</header>

<section class="abs hero">
  <p class="abs hero-text">Lorem Ipsum is simply dummy text of the printing and type-setting industry. Lorem Ipsum has been the industry's standard dummy text ever since the 1500s, when an unknown printer took a galley of type and scrambled it to make a type specimen book.</p>
  <div class="btn btn-outline" style="left:233px;top:315px;width:157px;height:33px">SHOP NOW</div>
  <div class="photo" role="img" aria-label="Crystal glass holders and a business card on display" style="left:686px;top:160px;width:374px;height:320px;border-radius:24px;background:linear-gradient(160deg,#e8f1f5 0%,#c4d7e0 60%,#9fb9c7 100%)"></div>
</section>

<section>
  <h2 class="title" style="top:734px">About Us</h2>
  <p class="abs copy" style="left:233px;top:810px;width:735px">Lorem Ipsum is simply dummy text of the printing and typesetting industry. Lorem Ipsum has been the industry's standard dummy text ever since the 1500s, anun-printer took a galley of type and scrambled it to make a type specimen book.</p>
  <p class="abs copy" style="left:233px;top:880px;width:350px">Lorem Ipsum is simply dummy text of the printing and typesetting industry. Lorem Ipsum has been the industry's standard dummy text ever since the 1500s, when an unknown printer took a galley of type and scrambled it to make a type specimen book.</p>
  <div class="photo" role="img" aria-label="Bright Willow Care business card with a lotus flower" style="left:652px;top:883px;width:312px;height:210px;background:linear-gradient(135deg,#f3eef0 0%,#d9d0d8 45%,#8f7a6a 100%)"></div>
  <div class="btn btn-solid" style="left:233px;top:1062px;width:155px;height:31px">LEARN MORE</div>
</section>

<section>
  <h2 class="title" style="top:1206px">Our Services</h2>
  <p class="abs copy" style="left:233px;top:1279px;width:740px">Lorem Ipsum is simply dummy text of the printing and typesetting industry. Lorem Ipsum has been the industry's standard dummy text ever since the 1500s, when an unknown printer took a galley of type and scrambled it to make a type specimen book.Lorem Ipsum is simply dummy text of the printing and typesetting industry. Lorem Ipsum has been the industry's standard dummy text ever since the 1500s, when an unknown printer took a galley of type and scrambled it to make a type specimen book.</p>

  <div class="abs service" style="left:233px;top:1478px">
    <svg width="46" height="36" viewBox="0 0 46 36" fill="#00bdf2"><rect x="0" y="0" width="8" height="6"/><rect x="12" y="0" width="34" height="6"/><rect x="0" y="10" width="8" height="6"/><rect x="12" y="10" width="34" height="6"/><rect x="0" y="20" width="8" height="6"/><rect x="12" y="20" width="34" height="6"/><rect x="0" y="30" width="8" height="6"/><rect x="12" y="30" width="34" height="6"/></svg>
    Lorem Ipsum is simply dummy text of the print-ing and typesetting in-dustry
  </div>
  <div class="abs service" style="left:514px;top:1478px">
    <svg width="30" height="44" viewBox="0 0 30 44"><text x="15" y="38" text-anchor="middle" font-family="Poppins,sans-serif" font-weight="700" font-size="44" fill="#00bdf2">$</text></svg>
    Lorem Ipsum is simply dummy text of the print-ing and typesetting in-dustry
  </div>
  <div class="abs service" style="left:793px;top:1472px">
    <svg width="52" height="34" viewBox="0 0 52 34" fill="#00bdf2"><rect x="0" y="2" width="32" height="22" rx="2"/><path d="M34,8 H44 L52,17 V24 H34Z"/><circle cx="10" cy="27" r="5"/><circle cx="42" cy="27" r="5"/></svg>
    Lorem Ipsum is simply dummy text of the print-ing and typesetting in-dustry
  </div>
  <div class="abs service" style="left:233px;top:1632px">
    <svg width="44" height="44" viewBox="0 0 44 44"><circle cx="18" cy="18" r="14" fill="none" stroke="#00bdf2" stroke-width="5"/><path d="M18,10 l8,7 h-3 v7 h-10 v-7 h-3z" fill="#00bdf2"/><line x1="28" y1="28" x2="41" y2="41" stroke="#00bdf2" stroke-width="6"/></svg>
    Lorem Ipsum is simply dummy text of the print-ing and typesetting in-dustry
  </div>
  <div class="abs service" style="left:514px;top:1632px">
    <svg width="44" height="40" viewBox="0 0 44 40" fill="#00bdf2"><path d="M0,2 H8 L12,24 H38 L44,8 H10" fill="none" stroke="#00bdf2" stroke-width="4"/><rect x="11" y="9" width="30" height="13"/><circle cx="15" cy="33" r="4"/><circle cx="35" cy="33" r="4"/></svg>
    Lorem Ipsum is simply dummy text of the print-ing and typesetting in-dustry
  </div>
</section>

<section>
  <h2 class="title" style="top:1880px">Our Products</h2>
  <p class="abs copy" style="left:242px;top:1952px;width:735px">Lorem Ipsum is simply dummy text of the printing and typesetting industry. Lorem Ipsum has been the industry's standard dummy text ever since the 1500s, when an unknown printer took a galley of type and scrambled it to make a type specimen book.</p>
  <ul class="abs checks">
    <li><svg width="24" height="20" viewBox="0 0 24 20"><path d="M2,10 L9,17 L22,2" fill="none" stroke="#1a1a1a" stroke-width="4"/></svg>Lorem Ipsum is simply dummy text of the printing and typesetting industry.</li>
    <li><svg width="24" height="20" viewBox="0 0 24 20"><path d="M2,10 L9,17 L22,2" fill="none" stroke="#1a1a1a" stroke-width="4"/></svg>Lorem Ipsum is simply dummy text of the printing and typesetting industry.</li>
    <li><svg width="24" height="20" viewBox="0 0 24 20"><path d="M2,10 L9,17 L22,2" fill="none" stroke="#1a1a1a" stroke-width="4"/></svg>Lorem Ipsum is simply dummy text of the printing and typesetting industry.</li>
  </ul>
  <div class="abs" style="left:640px;top:2043px;display:grid;grid-template-columns:repeat(3,92px);column-gap:24px;row-gap:24px">
    <div class="thumb" role="img" aria-label="Singing bowl product photo"></div>
    <div class="thumb" role="img" aria-label="Singing bowl product photo"></div>
    <div class="thumb" role="img" aria-label="Singing bowl product photo"></div>
    <div class="thumb" role="img" aria-label="Singing bowl product photo"></div>
    <div class="thumb" role="img" aria-label="Singing bowl product photo"></div>
    <div class="thumb" role="img" aria-label="Singing bowl product photo"></div>
  </div>
  <div class="btn btn-solid" style="left:233px;top:2226px;width:155px;height:31px">SEE MORE</div>
</section>

<section class="abs cta">
  <div class="photo" role="img" aria-label="Smartphone showing the shop" style="left:236px;top:36px;width:183px;height:369px;border-radius:28px;background:linear-gradient(160deg,#2a2a2a,#0e0e0e)"></div>
  <h2 class="abs cta-title">GET YOUR PRODUCT NOW !</h2>
  <div class="btn btn-outline" style="left:631px;top:274px;width:186px;height:37px;font-size:19px">BOOK NOW</div>
</section>

<section>
  <h2 class="title" style="top:2930px">CONTACT US</h2>
  <p class="abs copy" style="left:233px;top:3005px;width:378px">Lorem Ipsum is simply dummy text of the printing and typesetting industry. Lorem Ipsum has been the industry's standard dummy text ever since the 1500s, when an unknown printer took a galley of type and scrambled it to make a type speci-men book. It has survived not only five centuries, but also the leap into electronic typesetting, remaining essentially un-changed.</p>
  <div class="field" style="top:3010px;height:33px"><span class="tag"><svg width="16" height="18" viewBox="0 0 16 18" fill="#1a3a5a"><circle cx="8" cy="5" r="4.5"/><path d="M0,18 C0,10 16,10 16,18Z"/></svg></span><span class="label">Name</span></div>
  <div class="field" style="top:3067px;height:33px"><span class="tag"><svg width="20" height="14" viewBox="0 0 20 14"><rect width="20" height="14" fill="#1a3a5a"/><path d="M0,0 L10,8 L20,0" fill="none" stroke="#0c70b8" stroke-width="1.5"/></svg></span><span class="label">Email</span></div>
  <div class="field" style="top:3124px;height:128px"><span class="abs" style="left:12px;top:6px">Your Text Here</span></div>
  <div class="btn btn-solid" style="left:631px;top:3283px;width:155px;height:30px">SUBMIT</div>
</section>

<footer class="abs footer">
  <div class="abs footer-brand">Bright Willow</div>
  <div class="abs" style="left:402px;top:12px">
    <h4>Contact Us</h4>
    <p style="margin-top:8px">4820 Willow Lane NE, Springvale<br>505-555-0142<br>info@brightwillowcare.com.au</p>
  </div>
  <div class="abs" style="left:674px;top:14px">
    <h4>Legal Info</h4>
    <p style="margin-top:6px">Terms Of Use<br>Privacy Policy<br>Copyright Policy</p>
  </div>
  <div class="abs" style="left:881px;top:18px">
    <h4>Follow Us</h4>
    <div style="margin-top:18px"><span class="sq"></span><span class="sq"></span><span class="sq"></span></div>
  </div>
  <div class="abs" style="left:0;top:116px;width:1200px;text-align:center;font-size:8px">Copyright © 2018 Bright Willow Care</div>
</footer>

</body>
</html>
```